Human Resources consulting firm website

I recently started a consulting firm after 30 years in Human Resources (Executive Development) work with Meridian 25 companies. I am looking for a website design that will convey both the services I provide (all in the HR / executive development arena) as well as sense of trust in me and my abilities (many years of experience, breadth of knowledge).

In the attachment section, there is a document with links to a number of websites fr firms that do similar work to me - the doc shares what I like about them and what I do not. I've also include my bio to give you a sens of who I am /what I do. The head shot will be replaced soon as I'm having new photos take, but the verbiage is what's important.

I need your help with the look and feel as well as different ideas on how to share the info. I am looking for your creativity and experience. I have not done a website for anything in the past.

Looking forward to working together on a great project and product!!

Target Market(s)

Any company looking for senior leader caoching, assessments of those leaders or help with a CEO transition. My wheelhouse is Meridian top 100 companies, but am able to work with small firms as well. Also any Board of Directors and upstarts in California.

Industry/Entity Type

Consulting

Coding

Coded - Design and coding required

Number of Pages Required

5+ page

Font styles to use
Sans Serif
Other font styles liked:
• Do not have a specific one but am very open to options

Colors

Designer to choose colors to be used in the design.

Requirements
Must have
• My project must have be professional (see the type of companies I am targeting) with an air of simplicity.
• A professional yet approachable look and feel that delivers:
• (1) I want there to be a landing page (with limited info - a more of a "teaser")
• (2) a tab for about us (with a few sentences about the company, my photo and option to link to my bio)
• (3) a tab for the services offered (one page with tiles that have a little bit about the services and the option to link to more info)
• (4) a tab to contact me (form to fill out with some personal info and the request that will get sent to my email).
• (5) diversity in the imagery
• (6) I plan for it to be mostly static. I will not be adding/changing regularly (although imagine the first couple months will want to tweak it as I get feedback). I do not plan to add blogs, etc.
Nice to have
• (1) Good graphics. I'm ok with black and white if it's classic or color photos. I don't want stalk photos anyone can get on the web. A sophisticated yet approachable look is what I'm going for.
• (2) Ability to get to know me (the principal) just a bit. That can be through the verbiage, colors, photos, etc.
• (3) Ability to contact me from the front home/landing page or contact page.
• (4) When someone looks me up on line, I want them to see a sentence or two about the company and have links that will take them straight to the page on the website they are looking for (contact, about us, etc.)
Should not have
• I do not want this to be:
• (1) overly feminine (not pink, purple, etc.),
• (2) flashy (I'm fine with a small video or moving photo but doubt I want anything beyond that) or
• (3) too close to the "out there" category (this is a professional business with corporate clients).
• (4) sterile (I'm selling myself .. that's what people buy when they hire a consultant).
• (5) basic - I do not want this to look like I hired my nephew straight out of college to build this. I'm looking for a strong, professional look.

```html
<!DOCTYPE html>
<html lang="en">
<head>
<meta charset="utf-8">
<title>Halloway Talent Partners — Human Resources Consulting</title>
<link href="https://fonts.googleapis.com/css2?family=Source+Sans+3:wght@300;400;600;700&display=swap" rel="stylesheet">
<style>
:root{
  --ink:#1f2024;
  --nav:#232428;
  --hero:#6689b5;
  --hero-light:#7a9cc6;
  --accent:#7ea2cf;
  --accent-dark:#5f84b3;
  --mist:#e4e4e6;
  --mist-soft:#ececed;
  --slate:#6c707f;
  --field:#34373f;
  --white:#ffffff;
  --muted:#4a4c52;
}
*{box-sizing:border-box;margin:0;padding:0}
html,body{width:1200px;height:2738px;overflow:hidden}
body{position:relative;font-family:"Source Sans 3",sans-serif;color:var(--ink);background:var(--white)}
.abs{position:absolute}
a{color:inherit;text-decoration:none}

/* header */
.site-header{position:absolute;left:0;top:0;width:1200px;height:100px;background:var(--white);border-bottom:4px solid var(--nav)}
.brand{position:absolute;left:143px;top:12px;display:flex;align-items:center;gap:14px}
.brand-mark{width:18px;height:18px;background:var(--accent)}
.brand-name{border-left:2px solid #b9bcc4;padding-left:12px;font-size:21px;line-height:21px;font-weight:600;color:var(--accent-dark);text-transform:uppercase;letter-spacing:.5px}
.topbar{position:absolute;right:155px;top:8px;display:flex;align-items:center;gap:10px;font-size:16px}
.topbar .label{font-weight:600}
.topbar .phone{color:#8b8d93;font-weight:600}
.topbar .sep{width:1px;height:26px;background:#555;margin:0 14px}
.social{width:28px;height:28px;border:1.5px solid var(--accent);border-radius:50%;margin-left:10px}
.nav-band{position:absolute;left:420px;top:44px;width:780px;height:56px;background:var(--nav);clip-path:polygon(22px 0,100% 0,100% 100%,0 100%)}
.nav{position:absolute;left:496px;top:62px;display:flex;gap:38px;font-size:12.5px;font-weight:700;color:var(--white)}
.nav .current{color:var(--accent);border-bottom:2px solid var(--accent);padding-bottom:4px}
.search{position:absolute;left:893px;top:58px;width:152px;height:30px;border-radius:15px;background:#4b4e55;color:#b9bbc0;font-size:13px;padding:6px 14px}

/* hero */
.hero{position:absolute;left:0;top:100px;width:1200px;height:673px;background:var(--hero);overflow:hidden}
.hero-glow{position:absolute;left:-250px;top:-230px;width:520px;height:780px;border-radius:50%;background:#5d80ab}
.hero-paper{position:absolute;left:740px;top:0;width:460px;height:260px;background:var(--hero-light)}
.hero-disc{position:absolute;left:640px;top:200px;width:620px;height:620px;border-radius:50%;background:#d8d9dc}
.hero-figure{position:absolute;left:755px;top:40px;width:330px;height:633px;background:linear-gradient(180deg,#c9cbcf 0%,#5a5d63 30%,#26272b 60%,#1d1e22 100%);border-radius:120px 120px 0 0}
.hero-title{position:absolute;left:143px;top:106px;color:var(--ink)}
.hero-title .lead{font-size:70px;font-weight:300;line-height:70px;letter-spacing:-1px}
.hero-title .name{font-size:74px;font-weight:700;line-height:75px;color:var(--white);margin-top:18px;text-transform:uppercase}
.hero-sub{position:absolute;left:144px;top:448px;font-size:25px;color:var(--white);font-weight:400}
.btn{display:inline-flex;align-items:center;justify-content:center;gap:10px;border-radius:24px;font-size:14px;text-transform:uppercase}
.btn svg{width:24px;height:10px}
.btn-dark{background:var(--nav);color:var(--white)}
.btn-ghost{border:1.5px solid var(--ink);color:var(--ink)}
.hero-read{position:absolute;left:143px;top:512px;width:155px;height:44px}
.hero-contact{position:absolute;left:312px;top:512px;width:155px;height:44px}
.dots{position:absolute;left:29px;top:371px;display:flex;flex-direction:column;gap:13px}
.dots span{width:14px;height:14px;border-radius:50%;background:#4a4d55}
.dots .on{background:#111}

/* about */
.deco-circle{position:absolute;left:-214px;top:1108px;width:620px;height:740px;border-radius:50%;background:var(--mist-soft)}
.about-panel{position:absolute;left:143px;top:880px;width:902px;height:472px;background:var(--mist)}
.about-photo{position:absolute;left:143px;top:880px;width:314px;height:472px;background:linear-gradient(180deg,#f0f0f0 0%,#cdb8a8 35%,#2a2426 70%,#141214 100%)}
.about-frame{position:absolute;left:164px;top:859px;width:295px;height:512px;border:1.5px solid var(--accent)}
.about-head{position:absolute;left:504px;top:950px;font-size:34px;line-height:40px;font-weight:400}
.about-head strong{display:block;color:var(--accent);font-weight:700;font-size:34px}
.about-copy{position:absolute;left:504px;top:1047px;width:500px;font-size:13px;line-height:19.5px;color:var(--muted)}
.btn-bio{position:absolute;left:505px;top:1249px;width:112px;height:32px;background:var(--accent);color:var(--white);font-size:13px}

/* services */
.services-title{position:absolute;left:0;top:1488px;width:1200px;text-align:center;font-size:43px;font-weight:700;color:var(--accent)}
.services-rule{position:absolute;left:573px;top:1543px;width:44px;height:2px;background:#8f9196}
.service{position:absolute;top:1588px;width:268px;height:268px;border-radius:50%;overflow:hidden}
.service.photo{background:linear-gradient(160deg,#7fa0a6 0%,#cfd6d2 45%,#6a5f58 100%)}
.service.photo .cap{position:absolute;left:0;right:0;bottom:0;height:60px;background:var(--white);border-radius:50% 50% 0 0/40px 40px 0 0}
.service-label{position:absolute;top:1822px;width:268px;text-align:center;font-size:23px;font-weight:600;color:var(--ink)}
.service.feature{background:#34363b;color:var(--white);text-align:center}
.service.feature h3{margin-top:70px;font-size:24px;font-weight:600}
.service.feature p{width:196px;margin:14px auto 0;font-size:8.5px;line-height:12.5px}
.service.feature .more{margin-top:12px;font-size:10px;display:inline-flex;gap:8px;align-items:center}
.btn-all{position:absolute;left:521px;top:1896px;width:150px;height:36px}

/* call to action */
.cta{position:absolute;left:0;top:2046px;width:1200px;height:409px;background:var(--slate)}
.cta-figure{position:absolute;left:143px;top:2083px;width:250px;height:372px;background:linear-gradient(180deg,#c9a27a 0%,#e9d3c2 35%,#1c1c20 55%,#141418 100%);border-radius:110px 110px 0 0}
.cta-title{position:absolute;left:364px;top:2132px;font-size:47px;line-height:54px;font-weight:700;color:var(--white);text-transform:uppercase}
.cta-copy{position:absolute;left:369px;top:2244px;width:680px;font-size:13px;line-height:18px;color:var(--white)}
.subscribe{position:absolute;left:555px;top:2314px;width:490px;height:55px;background:var(--field);border-radius:3px}
.subscribe .field{position:absolute;left:22px;top:20px;width:340px;border-bottom:1px solid #4d5058;font-size:9px;color:#8a8d94;padding-bottom:4px}
.subscribe .go{position:absolute;left:375px;top:14px;width:97px;height:27px;background:var(--accent);color:var(--white);font-size:8.5px;text-transform:uppercase;display:flex;align-items:center;justify-content:center}

/* footer */
.footer-swoosh{position:absolute;left:0;top:2455px;width:1200px;height:250px}
.footer-brand{position:absolute;left:143px;top:2503px;display:flex;align-items:center;gap:18px}
.footer-brand .brand-mark{width:26px;height:26px}
.footer-brand .brand-name{font-size:30px;line-height:30px;padding-left:16px}
.footer-col{position:absolute;top:2500px}
.footer-col h4{font-size:25px;font-weight:600;text-transform:uppercase}
.footer-col .rule{width:34px;height:2px;background:var(--accent);margin:10px 0 14px}
.links li{list-style:none;font-size:12.5px;line-height:21px;margin-left:4px}
.links .current{color:var(--accent)}
.contact-row{display:flex;align-items:center;gap:20px;font-size:12.5px;height:38px}
.contact-row svg{width:16px;height:16px}
.copyright{position:absolute;left:0;top:2705px;width:1200px;height:33px;background:var(--accent);color:var(--white);font-size:12.5px;text-align:center;line-height:33px}
</style>
</head>
<body>

<header class="site-header">
  <div class="brand"><span class="brand-mark"></span><span class="brand-name">Halloway<br>Talent<br>Partners</span></div>
  <div class="topbar">
    <svg width="26" height="26" viewBox="0 0 26 26"><circle cx="13" cy="13" r="12" fill="none" stroke="#111" stroke-width="2"/><path d="M8 7l3 0 1 4-2 1c1 2 2 3 4 4l1-2 4 1 0 3c-6 1-12-5-11-11z" fill="#111"/></svg>
    <span class="label">Call Us Now:</span><span class="phone">(555)-014 2290</span>
    <span class="sep"></span>
    <span class="social" aria-label="Profile link"></span><span class="social" aria-label="Email link"></span><span class="social" aria-label="Website link"></span>
  </div>
  <div class="nav-band"></div>
  <nav class="nav"><a class="current">HOME</a><a>ABOUT US</a><a>SERVICES</a><a>CONTACT ME</a></nav>
  <div class="search">Search
    <svg class="abs" style="left:124px;top:6px" width="18" height="18" viewBox="0 0 18 18"><circle cx="7.5" cy="7.5" r="6" fill="none" stroke="#fff" stroke-width="2"/><line x1="12" y1="12" x2="17" y2="17" stroke="#fff" stroke-width="2"/></svg>
  </div>
</header>

<section class="hero">
  <div class="hero-glow"></div>
  <div class="hero-paper" role="img" aria-label="Business newspaper on a desk"></div>
  <div class="hero-disc" role="img" aria-label="Laptop on a desk in soft grey"></div>
  <div class="hero-figure" role="img" aria-label="Figure in a dark suit with a light bulb in place of a head"></div>
  <h1 class="hero-title"><div class="lead">WELCOME TO</div><div class="name">Halloway<br>Talent<br>Partners</div></h1>
  <p class="hero-sub">HUMAN RESOURCES CONSULTING FIRM</p>
  <a class="btn btn-dark hero-read">Read more <svg viewBox="0 0 24 10"><path d="M0 5h22M17 1l5 4-5 4" fill="none" stroke="#fff" stroke-width="1.3"/></svg></a>
  <a class="btn btn-ghost hero-contact">Contact me <svg viewBox="0 0 24 10"><path d="M0 5h22M17 1l5 4-5 4" fill="none" stroke="#1f2024" stroke-width="1.3"/></svg></a>
</section>
<div class="dots"><span></span><span></span><span class="on"></span><span></span></div>

<div class="deco-circle"></div>

<section class="about">
  <div class="about-panel"></div>
  <div class="about-photo" role="img" aria-label="Portrait of the firm's principal"></div>
  <div class="about-frame"></div>
  <h2 class="about-head">ABOUT<strong>HALLOWAY TALENT PARTNERS</strong></h2>
  <p class="about-copy">Lorem ipsum dolor sit amet, consectetur adipiscing elit, sed do eiusmod tempor incididunt ut labore et dolore magna aliqua. Ut enim ad minim veniam, quis nostrud exercitation ullamco laboris nisi ut aliquip ex ea commodo consequat. Duis aute irure dolor in reprehenderit in voluptate velit esse cillum dolore eu fugiat nulla pariatur. Excepteur sint occaecat cupidatat non proident, sunt in culpa qui officia deserunt mollit anim id est laborum.Sed ut perspiciatis unde omnis iste natus error sit voluptatem accusantium doloremque laudantium, totam rem aperiam, eaque ipsa quae ab illo inventore veritatis et quasi architecto beatae vitae dicta sunt explicabo. Nemo enim ipsam voluptatem quia voluptas sit aspernatur aut odit aut fugit, sed quia consequuntur magni dolores eos qui ratione voluptatem sequi nesciunt.</p>
  <a class="btn btn-bio">My bio <svg viewBox="0 0 24 10"><path d="M0 5h22M17 1l5 4-5 4" fill="none" stroke="#fff" stroke-width="1.3"/></svg></a>
</section>

<section class="services">
  <h2 class="services-title">OUR SERVICES</h2>
  <div class="services-rule"></div>
  <div class="service photo" style="left:142px" role="img" aria-label="Hands reviewing charts beside a laptop"><div class="cap"></div></div>
  <div class="service-label" style="left:142px">SERVICE 1</div>
  <div class="service feature" style="left:460px">
    <h3>SERVICE 2</h3>
    <p>Lorem ipsum dolor sit amet, consectetur adipiscing elit, sed do eiusmod tempor incididunt ut labore et dolore magna aliqua. Ut enim ad minim veniam, quis nostrud exercitation ullamco laboris nisi ut aliquip ex ea commodo consequat.</p>
    <a class="more">READ MORE <svg width="20" height="8" viewBox="0 0 24 10"><path d="M0 5h22M17 1l5 4-5 4" fill="none" stroke="#fff" stroke-width="1.3"/></svg></a>
  </div>
  <div class="service photo" style="left:777px" role="img" aria-label="Hands reviewing charts beside a laptop"><div class="cap"></div></div>
  <div class="service-label" style="left:777px">SERVICE 1</div>
  <a class="btn btn-dark btn-all">All services <svg viewBox="0 0 24 10"><path d="M0 5h22M17 1l5 4-5 4" fill="none" stroke="#fff" stroke-width="1.3"/></svg></a>
</section>

<section class="cta"></section>
<div class="cta-figure" role="img" aria-label="Smiling professional woman with arms crossed"></div>
<h2 class="cta-title">Lorem ipsum dolor sit amet,<br>consectetur adipiscing elit</h2>
<p class="cta-copy">Lorem ipsum dolor sit amet, consectetur adipiscing elit, sed do eiusmod tempor incididunt ut labore et dolore magna aliqua. Ut enim ad minim veniam, quis nostrud exercitation ullamco laboris nisi ut aliquip ex ea commodo consequat.</p>
<form class="subscribe"><div class="field">Your E-Mail Address</div><div class="go">Subscribe now</div></form>

<footer>
  <svg class="footer-swoosh" viewBox="0 0 1200 250" preserveAspectRatio="none"><path d="M960 30 L1200 20 L1200 200 C1120 120 1040 80 960 30Z" fill="#e6e6e8"/><path d="M1040 150 C1110 160 1160 190 1200 230 L1200 250 C1150 210 1100 180 1040 150Z" fill="#e6e6e8"/></svg>
  <div class="footer-brand"><span class="brand-mark"></span><span class="brand-name">Halloway<br>Talent<br>Partners</span></div>
  <div class="footer-col" style="left:562px">
    <h4>Quick links</h4><div class="rule"></div>
    <ul class="links"><li class="current">HOME</li><li>ABOUT US</li><li>SERVICES</li><li>CONTACT ME</li></ul>
  </div>
  <div class="footer-col" style="left:796px">
    <h4>Address</h4><div class="rule"></div>
    <div class="contact-row"><svg viewBox="0 0 16 16"><path d="M2 1h4l1 4-2 1c1 2 3 4 5 5l1-2 4 1v4C8 15 1 8 2 1z" fill="#7ea2cf"/></svg>(555)-014 2290</div>
    <div class="contact-row"><svg viewBox="0 0 16 16"><path d="M1 8L15 2 11 15 8 10z" fill="#7ea2cf"/></svg>Dana@HallowayTalentPartners.com</div>
    <div class="contact-row"><svg viewBox="0 0 16 16"><circle cx="8" cy="8" r="6.5" fill="none" stroke="#7ea2cf" stroke-width="1.3"/><path d="M1.5 8h13M8 1.5v13M3 4.5h10M3 11.5h10" stroke="#7ea2cf" stroke-width="1"/></svg>HallowayTalentPartners.com</div>
  </div>
  <div class="copyright">Copyright © HallowayTalentPartners 2020. All rights reserved.</div>
</footer>

</body>
</html>
```